Stonebrook Glazeworks Inc. Business Card

Looking for business card with embossed raised logo print. Logo provided and want it to be most prominent image on card. Color pallet of black, red, white or charcoal gray preferred for brand recognition. Simple contact information on front and list description of services provided on back. Services included....Custom Showers, Tub Surrounds, Backsplashes, Fireplaces, Floors and more. Dustless Demolition, Lifetime Warranty, Proud member of the Federated Surface Installers Guild

Target Market(s)

High end residential remodel work and new home builders

Contact Information for Business Card

Phone # (402) 555-0193 email address, Stonebrookgw@mailvane.net Dorian Kovalski Owner

Requirements
Must have
• Business logo as most prominent image on the front of business card. Along with contact information and name Dorian Kovalski. Would like to see services provided on the back of the card.

```html
<!DOCTYPE html>
<html lang="en">
<head>
<meta charset="utf-8">
<title>Stonebrook Glazeworks Inc. – Business Card</title>
<link rel="stylesheet" href="https://fonts.googleapis.com/css2?family=Arimo:wght@400;700&display=swap">
<style>
  :root {
    --backdrop: #e9e9e9;
    --charcoal: #333333;
    --charcoal-deep: #262626;
    --brand-red: #e0242b;
    --paper: #ffffff;
    --ink: #1f1f1f;
    --rule: #3a3a3a;
  }
  * { box-sizing: border-box; margin: 0; padding: 0; }
  html, body {
    width: 1200px; height: 801px; overflow: hidden;
    background: var(--backdrop);
    font-family: "Arimo", Arial, sans-serif;
  }
  .stage { position: relative; width: 1200px; height: 801px; }

  .card {
    position: absolute;
    width: 540px; height: 309px;
    box-shadow: 0 10px 24px rgba(0,0,0,.18);
  }

  /* Back of card – services */
  .card-back {
    left: 40px; top: 130px;
    background: linear-gradient(160deg, var(--charcoal) 0%, var(--charcoal-deep) 100%);
    border-bottom: 4px solid var(--brand-red);
    border-left: 4px solid var(--brand-red);
    color: var(--paper);
  }
  .card-back .brand-name {
    position: absolute; right: 30px; top: 34px;
    font-weight: 700; font-size: 27px; letter-spacing: .5px;
    color: var(--brand-red);
  }
  .card-back .services-heading {
    position: absolute; right: 30px; top: 84px;
    font-weight: 700; font-size: 15px; letter-spacing: .5px;
    color: var(--brand-red);
  }
  .services-list {
    position: absolute; right: 30px; top: 116px;
    list-style: none; text-align: right;
    font-size: 15px; line-height: 24px;
  }
  .services-list .bullet { color: var(--brand-red); margin: 0 4px; }

  /* Front of card – contact */
  .card-front {
    left: 620px; top: 360px;
    background: var(--paper);
    border-bottom: 4px solid var(--brand-red);
    border-right: 4px solid var(--brand-red);
  }
  .front-brand {
    position: absolute; left: 30px; top: 132px;
    display: flex; align-items: center; gap: 10px;
  }
  .front-brand .brand-square {
    width: 30px; height: 30px; background: var(--brand-red);
  }
  .front-brand .brand-name {
    font-weight: 700; font-size: 17px; color: var(--brand-red);
    width: 170px; line-height: 20px;
  }
  .divider {
    position: absolute; left: 262px; top: 96px;
    width: 1.5px; height: 110px; background: var(--rule);
  }
  .contact {
    position: absolute; left: 282px; top: 100px;
    color: var(--ink);
  }
  .contact .person-name {
    font-weight: 700; font-size: 19px; color: var(--brand-red); letter-spacing: .3px;
  }
  .contact .person-title { font-size: 14px; margin: 4px 0 10px; }
  .contact .line {
    display: flex; align-items: center; gap: 7px;
    font-size: 14px; line-height: 22px;
  }
  .contact svg { width: 13px; height: 13px; fill: var(--brand-red); flex: none; }
</style>
</head>
<body>
<main class="stage">

  <section class="card card-back" aria-label="Card back: services">
    <div class="brand-name">STONEBROOK GLAZEWORKS INC.</div>
    <div class="services-heading">SERVICES</div>
    <ul class="services-list">
      <li>Custom Showers <span class="bullet">•</span> Tub Surrounds <span class="bullet">•</span> Backsplashes <span class="bullet">•</span> Fireplaces</li>
      <li><span class="bullet">•</span> Floors and more <span class="bullet">•</span> Dustless Demolition <span class="bullet">•</span> Lifetime Warranty</li>
      <li><span class="bullet">•</span> Proud member of the Federated Surface Installers Guild</li>
    </ul>
  </section>

  <section class="card card-front" aria-label="Card front: contact">
    <div class="front-brand">
      <span class="brand-square"></span>
      <span class="brand-name">STONEBROOK GLAZEWORKS INC.</span>
    </div>
    <div class="divider"></div>
    <div class="contact">
      <div class="person-name">DORIAN KOVALSKI</div>
      <div class="person-title">Owner</div>
      <div class="line">
        <svg viewBox="0 0 24 24" aria-hidden="true"><path d="M6.6 10.8a15.1 15.1 0 0 0 6.6 6.6l2.2-2.2c.3-.3.7-.4 1-.2 1.1.4 2.3.6 3.6.6.6 0 1 .4 1 1V20c0 .6-.4 1-1 1A17 17 0 0 1 3 4c0-.6.4-1 1-1h3.5c.6 0 1 .4 1 1 0 1.3.2 2.5.6 3.6.1.3 0 .7-.2 1z"/></svg>
        <span>(402) 555-0193</span>
      </div>
      <div class="line">
        <svg viewBox="0 0 24 24" aria-hidden="true"><path d="M2 5h20v14H2z M3 6l9 7 9-7" fill="none" stroke="#e0242b" stroke-width="0"/><path d="M2 5h20v2l-10 7L2 7z"/><path d="M2 9l10 7 10-7v10H2z"/></svg>
        <span>Stonebrookgw@mailvane.net</span>
      </div>
    </div>
  </section>

</main>
</body>
</html>
```